Copper Wagon
ideas, energy & innovation
Can you also please upload drafts of the letter headed paper, compliments slips and invoice drafts for me to also look at!

```html
<!DOCTYPE html>
<html lang="en">
<head>
<meta charset="utf-8">
<title>Copper Wagon – Stationery Set</title>
<link rel="stylesheet" href="https://fonts.googleapis.com/css2?family=Open+Sans:wght@400;700&display=swap">
<style>
:root{
  --stage:#3a3a3a;
  --stage-dark:#262626;
  --paper:#ffffff;
  --navy:#0b2f7a;
  --blue:#1c63c9;
  --sky:#5fb2ff;
  --green:#8cc63f;
  --green-dark:#5e9a24;
  --ink:#33404f;
  --muted:#8a96a6;
  --caption:#9a9a9a;
  --faint:#e9eef5;
}
*{margin:0;padding:0;box-sizing:border-box}
html,body{width:1200px;height:346px;overflow:hidden}
body{
  font-family:"Open Sans",Arial,sans-serif;
  background:radial-gradient(ellipse at 50% 40%,var(--stage) 0%,var(--stage-dark) 100%);
  position:relative;
}
.piece{position:absolute;box-shadow:0 2px 5px rgba(0,0,0,.5)}
.caption{position:absolute;font-size:5px;color:var(--caption);text-align:center}
.brand{display:flex;align-items:center;gap:3px;font-weight:700;color:var(--navy);white-space:nowrap}
.brand .mark{display:inline-block;background:var(--blue)}
.brand.on-dark{color:#fff}
.brand.on-dark .mark{background:var(--sky)}
.small{font-size:4px;line-height:6px;color:var(--ink)}

/* business cards */
.card{width:138px;height:84px;background:var(--paper)}
.card-blue{background:radial-gradient(ellipse at 70% 30%,var(--blue) 0%,var(--navy) 75%)}
.card .brand{position:absolute;font-size:9px}
.card .brand .mark{width:9px;height:9px}
.card-front .brand{left:10px;top:30px}
.card-front .details{position:absolute;right:10px;bottom:10px;text-align:right}
.card-swoosh{position:absolute;left:0;bottom:0;width:100%;height:12px;background:linear-gradient(90deg,var(--navy),var(--blue),var(--sky))}
.mini{width:66px;height:40px}
.tagline{position:absolute;font-size:4px;color:#cfe2ff}

/* letterheads */
.letter{width:220px;height:310px;background:var(--paper);top:18px}
.letter .brand{position:absolute;left:30px;top:14px;font-size:8px}
.letter .brand .mark{width:10px;height:10px}
.letter .details{position:absolute;left:102px;top:12px}
.letter-watermark{position:absolute;left:50%;top:50%;transform:translate(-50%,-50%);display:flex;align-items:center;gap:10px;font-weight:700;font-size:22px;color:var(--faint);white-space:nowrap}
.letter-watermark .mark{width:30px;height:30px;background:var(--faint)}
.letter-band{position:absolute;left:0;bottom:0;width:100%;height:14px;background:linear-gradient(90deg,var(--navy),var(--blue) 45%,var(--sky) 60%,var(--navy))}

/* compliment slips */
.slip{width:216px;height:86px;background:var(--paper);left:643px}
.slip .brand{position:absolute;left:12px;top:10px;font-size:6px}
.slip .brand .mark{width:7px;height:7px}
.slip .letter-watermark{font-size:12px;gap:6px}
.slip .letter-watermark .mark{width:18px;height:18px}
.slip .letter-band{height:6px}

/* envelopes */
.envelope{width:298px;height:92px;left:883px;overflow:hidden}
.envelope svg{position:absolute;left:0;top:0}
.envelope .brand{position:absolute;left:50%;transform:translateX(-50%);font-size:5px}
.envelope .brand .mark{width:6px;height:6px}
</style>
</head>
<body>

<!-- Business cards -->
<div class="piece card card-front" style="left:14px;top:26px">
  <div class="brand"><span class="mark"></span>CopperWagon</div>
  <div class="details small">Sam Reed<br>Director<br>T 0113 496 0000<br>hello@copperwagon.co</div>
  <div class="card-swoosh"></div>
</div>
<div class="caption" style="left:14px;top:114px;width:138px">Business cards</div>

<div class="piece card mini" style="left:14px;top:140px">
  <div class="brand" style="left:6px;top:14px;font-size:6px"><span class="mark" style="width:6px;height:6px"></span>CopperWagon</div>
</div>
<div class="piece card card-blue mini" style="left:86px;top:140px">
  <div class="brand on-dark" style="left:6px;top:12px;font-size:6px"><span class="mark" style="width:6px;height:6px"></span>CopperWagon</div>
  <div class="tagline" style="left:6px;top:24px">ideas, energy &amp; innovation</div>
</div>
<div class="piece card card-blue mini" style="left:14px;top:186px">
  <div class="card-swoosh" style="height:5px"></div>
</div>
<div class="piece card mini" style="left:86px;top:186px">
  <div class="card-swoosh" style="height:5px"></div>
</div>

<div class="piece card card-blue" style="left:14px;top:238px">
  <div class="brand on-dark" style="left:12px;top:30px;font-size:11px"><span class="mark" style="width:11px;height:11px"></span>CopperWagon</div>
  <div class="tagline" style="left:12px;top:48px;font-size:5px">ideas, energy &amp; innovation</div>
</div>

<!-- Letterheads -->
<div class="piece letter" style="left:168px">
  <div class="brand"><span class="mark"></span>CopperWagon</div>
  <div class="details small">12 Harbour Lane<br>Leeds LS1 4AB<br>T 0113 496 0000<br>hello@copperwagon.co</div>
  <div class="letter-watermark"><span class="mark"></span>CopperWagon</div>
  <div class="letter-band"></div>
</div>
<div class="caption" style="left:168px;top:332px;width:220px">Letterhead 01</div>

<div class="piece letter" style="left:403px">
  <div class="brand" style="left:30px"><span class="mark"></span>CopperWagon</div>
  <div class="letter-watermark"><span class="mark"></span>CopperWagon</div>
  <div class="letter-band"></div>
</div>
<div class="caption" style="left:403px;top:332px;width:220px">Letterhead 02</div>

<!-- Compliment slips -->
<div class="piece slip" style="top:124px">
  <div class="brand"><span class="mark"></span>CopperWagon</div>
  <div class="letter-watermark"><span class="mark"></span>CopperWagon</div>
  <div class="letter-band"></div>
</div>
<div class="caption" style="left:643px;top:212px;width:216px">Compliment slip</div>

<div class="piece slip" style="top:214px">
  <div class="brand"><span class="mark"></span>CopperWagon</div>
  <div class="letter-watermark"><span class="mark"></span>CopperWagon</div>
  <div class="letter-band"></div>
</div>
<div class="caption" style="left:643px;top:302px;width:216px">Compliment slip</div>

<!-- Envelopes -->
<div class="piece envelope" style="top:66px">
  <svg width="298" height="92" viewBox="0 0 298 92">
    <rect width="298" height="92" fill="var(--green)"/>
    <path d="M0 0 L149 58 L298 0 Z" fill="var(--paper)"/>
    <path d="M0 0 L149 58 L298 0" fill="none" stroke="var(--green-dark)" stroke-width="1"/>
  </svg>
  <div class="brand" style="top:8px"><span class="mark"></span>CopperWagon</div>
</div>
<div class="piece envelope" style="top:120px">
  <svg width="298" height="92" viewBox="0 0 298 92">
    <defs><linearGradient id="env-blue" x1="0" y1="0" x2="1" y2="0">
      <stop offset="0" stop-color="var(--navy)"/><stop offset=".5" stop-color="var(--blue)"/><stop offset="1" stop-color="var(--navy)"/>
    </linearGradient></defs>
    <rect width="298" height="92" fill="url(#env-blue)"/>
    <path d="M0 0 L149 58 L298 0 Z" fill="var(--paper)"/>
    <path d="M0 0 L149 58 L298 0" fill="none" stroke="var(--sky)" stroke-width="1"/>
  </svg>
  <div class="brand" style="top:8px"><span class="mark"></span>CopperWagon</div>
</div>
<div class="piece envelope" style="top:180px;height:128px;background:var(--paper)">
  <svg width="298" height="128" viewBox="0 0 298 128">
    <path d="M0 0 L149 62 L298 0" fill="none" stroke="#d5dbe3" stroke-width="1"/>
    <path d="M0 128 L120 60 M298 128 L178 60" fill="none" stroke="#e3e7ec" stroke-width="1"/>
  </svg>
  <div class="brand" style="top:10px"><span class="mark"></span>CopperWagon</div>
</div>
<div class="caption" style="left:883px;top:314px;width:298px">Envelopes</div>

</body>
</html>
```